Time for a new business card design

We need a new business card design for Tolvik Furniture Rentals based in Australia. www.tolvik-example.com.au. We specialise in providing furniture rentals for home staging, corporate relocations events and product launches etc. We would like to see designs that include our logo on the front of the card with all the standard contact details as well as having a realy nice image on the back with a list of our services we offer. Our logo is red and this cannot change. Were looking for a pallet of red and white with maybe a splash of grey. The final design should communication organised & stylish. We are in the process of finalising our new website and would like the card design to compliment this as well

Requirements
Must have
• Square corners
logo
name, title, email, phone, address
image on back of card with space for list of services we offer
Services:
•Furniture and appliance rental
•Property styling
•Events and functions
•Office furniture rental

The card must be landscape.
The image is to appear on the back of the card only.

```html
<!DOCTYPE html>
<html lang="en">
<head>
<meta charset="utf-8">
<title>Tolvik Furniture Rentals – Business Card</title>
<link rel="stylesheet" href="https://fonts.googleapis.com/css2?family=Open+Sans:ital,wght@0,400;0,700;1,700&display=swap">
<style>
  :root {
    --brand-red: #b0151f;
    --swoosh-grey: #c4c4c4;
    --ink: #333333;
    --paper: #ffffff;
    --backdrop: #2a3334;
  }
  * { box-sizing: border-box; margin: 0; padding: 0; }
  html, body { width: 914px; height: 1200px; overflow: hidden; }
  body {
    background: var(--backdrop);
    font-family: "Open Sans", Arial, sans-serif;
    color: var(--ink);
    position: relative;
  }
  .card {
    position: absolute;
    left: 59px;
    width: 801px;
    height: 457px;
    background: var(--paper);
    overflow: hidden;
  }
  .card--front { top: 105px; }
  .card--back { top: 672px; }

  .swoosh { position: absolute; }
  .swoosh--top { right: 0; top: 0; }
  .swoosh--bottom { left: 0; bottom: 0; }

  .wordmark {
    color: var(--brand-red);
    font-weight: 400;
    letter-spacing: -1px;
    white-space: nowrap;
  }
  .card--front .wordmark {
    position: absolute;
    left: 56px;
    top: 88px;
    font-size: 60px;
    line-height: 1;
  }
  .card--back .wordmark {
    position: absolute;
    left: 0; right: 0;
    top: 22px;
    text-align: center;
    font-size: 30px;
    line-height: 1;
  }

  .contact {
    position: absolute;
    left: 0; right: 0;
    top: 242px;
    text-align: center;
    font-size: 21px;
    line-height: 1;
  }
  .contact__name { font-size: 23px; font-weight: 700; }
  .contact__title { font-size: 19px; font-weight: 400; }
  .contact__line { margin-top: 20px; }
  .contact__line--address { margin-top: 33px; }
  .contact__label { font-weight: 700; font-style: italic; }
  .contact__sep { margin: 0 8px; }

  .services {
    position: absolute;
    top: 97px;
    left: 1px;
    display: flex;
    gap: 5px;
  }
  .service { width: 196px; }
  .service:nth-child(3) { margin-left: 5px; }
  .service__title {
    height: 55px;
    background: var(--brand-red);
    color: var(--paper);
    font-size: 19px;
    line-height: 23px;
    text-align: center;
    display: flex;
    align-items: center;
    justify-content: center;
  }
  .service__image { height: 300px; margin-top: 4px; }
  .service__image--kitchen { background: linear-gradient(180deg, #3b3a33 0%, #5a5850 55%, #c9c9c4 100%); }
  .service__image--lounge { background: linear-gradient(180deg, #e6e6e3 0%, #b9b5ad 60%, #c9a984 100%); }
  .service__image--event { background: radial-gradient(circle at 50% 45%, #e85a3a 0%, #6b1f4a 40%, #1b1230 100%); }
  .service__image--office { background: linear-gradient(180deg, #f2f2f2 0%, #d9d9d9 60%, #3b3b3b 100%); }
</style>
</head>
<body>

<section class="card card--front">
  <svg class="swoosh swoosh--top" width="240" height="90" viewBox="0 0 240 90">
    <path d="M40 0 C120 0 200 20 240 55 L240 82 C200 40 130 12 40 0 Z" fill="var(--swoosh-grey)"/>
    <path d="M0 0 L240 0 L240 58 C190 20 110 6 0 0 Z" fill="var(--brand-red)"/>
  </svg>
  <div class="wordmark">Tolvik Furniture Rentals</div>
  <div class="contact">
    <div><span class="contact__name">Your Name - </span><span class="contact__title">Designation</span></div>
    <div class="contact__line"><span class="contact__label">p</span> : 0123-456-789<span class="contact__sep">|</span><span class="contact__label">c</span> : 0123-456-789<span class="contact__sep">|</span><span class="contact__label">f</span> : 0123-456-789</div>
    <div class="contact__line"><span class="contact__label">e</span> : name@website.com<span class="contact__sep">|</span><span class="contact__label">w</span> : www.website.com</div>
    <div class="contact__line contact__line--address">1234 Main Street, Anytown, MD 21201</div>
  </div>
  <svg class="swoosh swoosh--bottom" width="220" height="85" viewBox="0 0 220 85">
    <path d="M0 0 C30 35 90 62 160 78 L110 78 C60 62 20 40 0 22 Z" fill="var(--swoosh-grey)"/>
    <path d="M0 22 C40 55 120 80 210 85 L0 85 Z" fill="var(--brand-red)"/>
  </svg>
</section>

<section class="card card--back">
  <div class="wordmark">Tolvik Furniture Rentals</div>
  <div class="services">
    <div class="service">
      <div class="service__title">Furniture and<br>appliance rental</div>
      <div class="service__image service__image--kitchen" role="img" aria-label="Photo of a modern kitchen with stainless steel appliances"></div>
    </div>
    <div class="service">
      <div class="service__title">Property styling</div>
      <div class="service__image service__image--lounge" role="img" aria-label="Photo of a styled living room with fireplace and coffee table"></div>
    </div>
    <div class="service">
      <div class="service__title">Events and<br>functions</div>
      <div class="service__image service__image--event" role="img" aria-label="Photo of an event hall with stage lighting and set tables"></div>
    </div>
    <div class="service">
      <div class="service__title">Office furniture<br>rental</div>
      <div class="service__image service__image--office" role="img" aria-label="Photo of an office with desk, chair and cabinets"></div>
    </div>
  </div>
</section>

</body>
</html>
```